Brightwater Health Partners, LLC Business Card update!

would like a classier business card. Our cards currently just have our logo and contact information. Need better use of color and creativity
Logo attached.

Target Market(s)

Potential clients, contacts, existing clients. We are a consulting company

Industry/Entity Type

Business

Contact Information for Business Card

We like our colors but just have a boring card with our logo and a white background. I want something that stands out.

Colors
ec1f27
757575

Requirements
Must have
• Color to stay consistent. Logo provided
Nice to have
• Just better use of color/ design

```html
<!DOCTYPE html>
<html lang="en">
<head>
<meta charset="utf-8">
<title>Brightwater Health Partners – Business Card</title>
<link rel="stylesheet" href="https://fonts.googleapis.com/css2?family=PT+Serif:ital,wght@0,400;0,700;1,400&display=swap">
<style>
  :root {
    --card-bg: #58585a;
    --brand-grey: #d2d2d3;
    --brand-red: #ec1f27;
    --text-light: #f4f4f4;
  }
  html, body {
    margin: 0;
    padding: 0;
    width: 1200px;
    height: 720px;
    overflow: hidden;
    background: var(--card-bg);
  }
  .card {
    position: relative;
    width: 1200px;
    height: 720px;
    background: var(--card-bg);
    font-family: "PT Serif", Georgia, serif;
    color: var(--text-light);
  }
  .brand-mark {
    position: absolute;
    left: 150px;
    top: 145px;
    width: 240px;
    height: 240px;
  }
  .brand-name {
    position: absolute;
    left: 330px;
    top: 92px;
    width: 790px;
    margin: 0;
    font-weight: 400;
    color: var(--brand-grey);
    text-align: right;
    line-height: 1;
  }
  .brand-name .brand-main {
    display: block;
    font-size: 100px;
    letter-spacing: 1px;
  }
  .brand-name .brand-sub {
    display: block;
    margin-top: 16px;
    font-size: 54px;
  }
  .contact {
    position: absolute;
    left: 464px;
    top: 418px;
    margin: 0;
    line-height: 1;
  }
  .contact p { margin: 0; }
  .contact .person-name {
    font-weight: 700;
    font-size: 37px;
    height: 52px;
  }
  .contact .company {
    font-size: 36px;
    height: 52px;
  }
  .contact .role {
    font-style: italic;
    font-size: 35px;
    height: 54px;
  }
  .contact .phone {
    font-size: 36px;
  }
</style>
</head>
<body>
  <main class="card">
    <svg class="brand-mark" viewBox="0 0 240 240" aria-hidden="true">
      <circle cx="120" cy="120" r="106" fill="none" stroke="var(--brand-red)" stroke-width="16"/>
    </svg>
    <h1 class="brand-name">
      <span class="brand-main">BRIGHTWATER</span>
      <span class="brand-sub">Health Partners</span>
    </h1>
    <section class="contact">
      <p class="person-name">Miriam Hollander</p>
      <p class="company">Brightwater Health Partners, LLC</p>
      <p class="role">founder and principal</p>
      <p class="phone">(555) 555-5555</p>
    </section>
  </main>
</body>
</html>
```